Harborlight Capital Estates business card

We are a real estate advisory and investment company. We are specialized in assisting high networth individuals to invest in real estate overseas. We deliver a very personalized service, anticipating all the potential challenges an investor can face, and making it easy and safe for them. We also co-invest with our clients, assuring them that each project will be looked after as it is our own, and at the same time giving them the extra booth on confidence to invest.

We need a business card design. The business card must have a very premium, high-end look, reflecting principles like "commitment", "trust" and "timeless (but contemporary)". We look for long term relationships with our clients, and we grow with their referrals. We are all about conquering the confidence of the clients by always delivering above the expectations performance.

Target Market(s)

High net worth individuals.

Industry/Entity Type

Real Estate

Contact Information for Business Card

Please consider places on the business card for:

Name
Function (bellow name in smaller size text)

Mobile phone
E-mail
Skype ID
WeChat ID

Adress (3 lines)

Also include the following locations references:
PORTUGAL * DUBAI * HONG KONG

Website: www.hcestates-example.com

Requirements
Must have
• Company Logo

```html
<!DOCTYPE html>
<html lang="en">
<head>
<meta charset="utf-8">
<title>Harborlight Capital Estates — Business Card</title>
<link href="https://fonts.googleapis.com/css2?family=Roboto:wght@300;400&display=swap" rel="stylesheet">
<style>
  :root {
    --stage: #3a3a3c;
    --card: #231f20;
    --accent: #29a8e0;
    --text-grey: #9a9a9a;
    --text-light: #bdbdbd;
    --skyline-top: #3b3a3b;
    --skyline-bottom: #2c2a2b;
  }
  * { margin: 0; padding: 0; box-sizing: border-box; }
  html, body { width: 1200px; height: 900px; overflow: hidden; }
  body {
    background: var(--stage);
    font-family: "Roboto", Arial, sans-serif;
    position: relative;
  }
  .card {
    position: absolute;
    width: 620px;
    height: 354px;
    background: var(--card);
    box-shadow: 0 12px 30px rgba(0,0,0,0.45);
    overflow: hidden;
  }
  .card-front { left: 80px; top: 60px; }
  .card-back { left: 500px; top: 486px; }

  .brand-name {
    position: absolute;
    color: var(--accent);
    font-weight: 400;
    letter-spacing: 2px;
    text-transform: uppercase;
    line-height: 1.15;
  }
  .card-front .brand-name { left: 150px; top: 92px; font-size: 26px; }
  .card-back .brand-name { left: 48px; top: 62px; font-size: 24px; }

  .locations {
    position: absolute;
    left: 150px;
    top: 176px;
    font-size: 14px;
    letter-spacing: 4px;
    color: var(--text-light);
    font-weight: 300;
  }
  .website {
    position: absolute;
    left: 260px;
    top: 212px;
    font-size: 12px;
    letter-spacing: 2px;
    color: var(--text-grey);
  }
  .website .domain { color: var(--accent); }

  .skyline {
    position: absolute;
    left: 0; right: 0; bottom: 0;
    height: 118px;
    background: linear-gradient(to bottom, var(--skyline-top), var(--skyline-bottom));
  }

  .divider {
    position: absolute;
    left: 210px;
    right: 36px;
    top: 206px;
    height: 1px;
    background: var(--accent);
  }
  .person-name {
    position: absolute;
    left: 60px;
    top: 186px;
    font-size: 20px;
    color: var(--accent);
  }
  .person-role {
    position: absolute;
    left: 72px;
    top: 212px;
    font-size: 14px;
    color: var(--accent);
  }
  .accent-bar {
    position: absolute;
    left: 0;
    top: 232px;
    width: 12px;
    height: 26px;
    background: var(--accent);
  }
  .address {
    position: absolute;
    left: 60px;
    bottom: 40px;
    font-size: 14px;
    line-height: 1.35;
    color: var(--text-grey);
  }
  .contacts {
    position: absolute;
    right: 36px;
    top: 70px;
    list-style: none;
    text-align: right;
  }
  .contacts li {
    display: flex;
    justify-content: flex-end;
    align-items: center;
    gap: 10px;
    font-size: 13px;
    line-height: 19px;
    color: var(--text-grey);
  }
  .contacts svg { width: 14px; height: 14px; flex: none; }
</style>
</head>
<body>

  <section class="card card-front" aria-label="Card front">
    <div class="brand-name">Harborlight<br>Capital Estates</div>
    <p class="locations">PORTUGAL * DUBAI * HONG KONG</p>
    <p class="website">www.<span class="domain">hcestates-example</span>.com</p>
    <div class="skyline" role="img" aria-label="Grey city skyline silhouette along the lower edge"></div>
  </section>

  <section class="card card-back" aria-label="Card back">
    <div class="brand-name">Harborlight<br>Capital Estates</div>

    <ul class="contacts">
      <li>555.014.2290
        <svg viewBox="0 0 14 14" aria-hidden="true"><rect x="3" y="0.5" width="8" height="13" rx="1.5" fill="none" stroke="#29a8e0" stroke-width="1.4"/><rect x="5.5" y="10.5" width="3" height="1.2" fill="#29a8e0"/></svg>
      </li>
      <li>DMarsh@hcestates-example.com
        <svg viewBox="0 0 14 14" aria-hidden="true"><rect x="0.5" y="2.5" width="13" height="9" fill="#29a8e0"/><path d="M0.5 2.5 L7 8 L13.5 2.5" fill="none" stroke="#231f20" stroke-width="1.2"/></svg>
      </li>
      <li>Daniel Marsh
        <svg viewBox="0 0 14 14" aria-hidden="true"><circle cx="7" cy="7" r="6" fill="#29a8e0"/></svg>
      </li>
      <li>Daniel Marsh
        <svg viewBox="0 0 14 14" aria-hidden="true"><circle cx="7" cy="7" r="6" fill="#29a8e0"/></svg>
      </li>
    </ul>

    <div class="divider"></div>
    <p class="person-name">Daniel Marsh</p>
    <p class="person-role">President</p>
    <div class="accent-bar"></div>

    <p class="address">2780 E. Lantern Ave.<br>Mesa, AZ 85204</p>
  </section>

</body>
</html>
```